Webdesign for an Health & Beauty Center

We need a new modern and elegant web design for the relaunch of the http://kirelta.at/ website.
The website is for a company which offer all services for a beuty center like epilation, cosmetics and more.
The new website should use big emotional background images and a modern menu.
All in all the website should give a female expression and the design should be clear and not playful.
The existing logo used be used for the new design, the base colours of the existing website could be used optionally.

Industry/Entity Type
It Company
Look and feel
Each slider illustrates characteristics of the customer's brand and the style your logo design should communicate.

```html
<!DOCTYPE html>
<html lang="en">
<head>
<meta charset="utf-8">
<title>Kirelta – Health &amp; Beauty Center</title>
<link href="https://fonts.googleapis.com/css2?family=Open+Sans:wght@400;600&family=Roboto:wght@300;400;500;700&display=swap" rel="stylesheet">
<style>
:root{
  --gold:#c8b07c;
  --gold-soft:#d6c395;
  --gold-line:#e4d7b8;
  --ink:#2f2f2f;
  --text:#555;
  --muted:#8c8c8c;
  --hero:#f6f0e4;
  --card:#fffdf8;
  --dark:#333333;
  --darker:#222222;
  --band:#d5c08f;
  --lime:#8fae22;
}
*{box-sizing:border-box;margin:0;padding:0}
html,body{width:1105px;height:1200px;overflow:hidden;background:#fff}
body{font-family:"Roboto",sans-serif;color:var(--text)}
.page{position:absolute;left:0;top:0;width:1300px;height:1412px;transform:scale(.85);transform-origin:0 0;background:#fff}
.abs{position:absolute}
.top-band{left:0;top:0;width:1300px;height:6px;background:var(--band)}
.top-notch{left:478px;top:0;width:64px;height:20px;background:var(--band);border-radius:0 0 32px 32px}
.brand{left:160px;top:22px;display:flex;align-items:center;gap:14px}
.brand-dot{width:46px;height:46px;border-radius:50%;background:var(--gold-soft)}
.brand-name{font-family:"Roboto",sans-serif;font-weight:300;font-size:64px;letter-spacing:6px;color:var(--gold);line-height:1}
.brand-tag{left:358px;top:94px;font-size:10px;letter-spacing:1px;color:var(--gold)}
.nav{left:484px;top:50px;display:flex;font-size:14.5px;color:var(--ink)}
.nav a{color:inherit;text-decoration:none;padding:0 13px;border-left:1px solid #ddd;line-height:18px;letter-spacing:.3px}
.nav a:first-child{border-left:0;padding-left:5px}
.nav a.active{font-weight:700;border-bottom:2px solid var(--gold);padding-bottom:3px}
.hero{left:160px;top:113px;width:980px;height:363px;background:var(--hero);border-radius:8px 8px 0 0;overflow:hidden}
.hero-photo{position:absolute;right:0;top:0;width:560px;height:363px;background:radial-gradient(ellipse at 60% 55%,#efd2b8 0%,#f2e2d0 40%,var(--hero) 72%)}
.hero h1{position:absolute;left:38px;top:40px;font-family:"Open Sans",sans-serif;font-weight:600;font-size:29px;line-height:40px;color:var(--ink)}
.hero p{position:absolute;left:36px;top:185px;width:360px;font-family:"Open Sans",sans-serif;font-size:14px;line-height:21px;color:#333}
.btn{position:absolute;left:38px;top:289px;width:90px;height:31px;background:var(--gold);color:#fff;font-family:"Open Sans",sans-serif;font-weight:600;font-size:13.5px;line-height:31px;text-align:center}
.dots{position:absolute;left:38px;top:338px;display:flex;gap:18px}
.dots span{width:14px;height:14px;border-radius:50%;background:#fff;box-shadow:0 1px 2px rgba(0,0,0,.25)}
.dots span.on{background:var(--gold)}
.card{width:311px;height:240px;top:537px}
.card svg.frame{position:absolute;left:0;top:0}
.card-icon{position:absolute;left:50%;top:-36px;margin-left:-37px;width:74px;height:74px;border-radius:50%;background:#fff;border:2px solid var(--gold-line);display:flex;align-items:center;justify-content:center}
.card-icon i{display:block;width:58px;height:58px;border-radius:50%;background:var(--gold-soft)}
.card h2{position:absolute;top:44px;width:100%;text-align:center;font-size:18px;font-weight:500;letter-spacing:1px;color:var(--gold)}
.card .rule{position:absolute;left:13px;right:13px;top:74px;height:1px;background:#d8cdb5}
.ticks{position:absolute;left:18px;top:88px;list-style:none;font-size:12.5px;line-height:19px;color:#333}
.ticks li{display:flex;align-items:center;gap:8px}
.card .more{position:absolute;top:205px;font-size:13px;font-weight:500;color:var(--gold);letter-spacing:.5px}
.card .pic{position:absolute}
.card .copy{position:absolute;left:18px;top:152px;width:275px;font-size:12.5px;line-height:16px;letter-spacing:.6px;color:#444}
.prices{position:absolute;left:35px;top:151px;width:240px;font-size:12.5px;line-height:17px;color:#444}
.prices div{display:flex}
.prices em{flex:1;font-style:normal;overflow:hidden;white-space:nowrap;margin:0 4px;color:#777;letter-spacing:1px}
.welcome{left:160px;top:805px;font-size:21px;color:#444}
.welcome b{font-weight:700;color:var(--gold);font-size:24px}
.welcome-text{left:160px;top:843px;width:646px;font-size:13px;line-height:19.5px;color:var(--muted);text-align:justify;letter-spacing:.15px}
.welcome-more{left:728px;top:987px;font-size:13px;font-weight:500;color:var(--gold)}
.offer{left:831px;top:819px;width:310px;height:174px;overflow:hidden;background:linear-gradient(90deg,#a8c22a 0%,#dfe86a 45%,#f4f3c0 100%)}
.offer-photo{position:absolute;right:0;top:0;width:175px;height:174px;background:radial-gradient(ellipse at 55% 50%,#f2cfae 0%,#efe2b8 45%,rgba(240,240,190,0) 75%)}
.offer-head{position:absolute;left:4px;top:4px;background:#fff;padding:2px 6px 2px 6px;font-weight:700;font-size:31px;line-height:29px;color:var(--lime)}
.offer-head span{display:block;font-weight:400;font-size:26px;letter-spacing:2px}
.offer-deal{position:absolute;left:9px;top:106px;font-weight:700;font-size:24px;color:#fff}
.offer-click{position:absolute;left:11px;top:144px;font-weight:700;font-size:14px;color:#fff}
.footer{left:0;top:1026px;width:1300px;height:353px;background:var(--dark);border-top:3px solid var(--gold-line)}
.news{left:160px;top:1058px;width:980px;height:82px;background:var(--darker);border:1px solid #555}
.news h3{position:absolute;left:12px;top:9px;font-weight:400;font-size:17px;color:var(--gold-soft)}
.news .field{position:absolute;left:12px;top:36px;width:487px;height:32px;background:#fff;font-size:14px;color:#999;line-height:32px;padding-left:12px}
.news .go{position:absolute;left:499px;top:36px;width:89px;height:32px;background:var(--band);color:#fff;font-weight:500;font-size:14px;line-height:32px;text-align:center}
.news .split{position:absolute;left:690px;top:6px;width:2px;height:68px;background:linear-gradient(#222,#3a3a3a,#222)}
.news h4{position:absolute;left:771px;top:9px;font-weight:400;font-size:17px;color:var(--gold-soft)}
.social{position:absolute;left:765px;top:40px;display:flex;gap:15px}
.social span{width:29px;height:29px;border-radius:50%;background:#9a9a9a}
.foot-h{font-weight:700;font-size:20px;color:var(--gold-soft)}
.thumb{top:1208px;width:120px;height:120px;border:1px solid var(--gold);padding:4px}
.thumb i{display:block;width:100%;height:100%}
.contact{left:653px;top:1205px;font-size:13.5px;color:var(--gold-soft)}
.contact li{list-style:none;display:flex;gap:12px;align-items:flex-start;margin-bottom:11px;line-height:19px}
.contact svg{flex:none;margin-top:1px}
.foot-brand{left:884px;top:1218px;display:flex;align-items:center;gap:10px}
.foot-brand .brand-dot{width:40px;height:40px;background:#6a6a6a}
.foot-brand .brand-name{font-size:56px;color:#7a7a7a}
.bottom{left:0;top:1379px;width:1300px;height:33px;background:var(--band);font-size:13px;color:#333;letter-spacing:.3px}
.bottom nav{position:absolute;left:160px;top:8px;display:flex}
.bottom nav a{color:inherit;text-decoration:none;padding:0 5px;border-left:1px solid #333;line-height:13px}
.bottom nav a:first-child{border:0;padding-left:0}
.bottom .copy{position:absolute;right:159px;top:8px}
</style>
</head>
<body>
<div class="page">
  <div class="abs top-band"></div>
  <div class="abs top-notch"></div>

  <div class="abs brand"><span class="brand-dot"></span><span class="brand-name">kirelta</span></div>
  <div class="abs brand-tag">HEALTH &amp; BEAUTY CENTER</div>

  <nav class="abs nav">
    <a class="active">Home</a><a>About Us</a><a>Our Services</a><a>Gallery</a><a>Care Line</a><a>Offers</a><a>Price Lists</a><a>Contact Us</a>
  </nav>

  <section class="abs hero">
    <div class="hero-photo" role="img" aria-label="Woman wrapped in a white towel sitting on a light background"></div>
    <h1>Lorem ipsum dolor sit amet, cons<br>sed diam nonummy nibh<br>reet dolore magna</h1>
    <p>Lorem ipsum dolor sit amet, consectetuer adipiscing elit, sed diam nonummy nibh euismod tincidunt ut laoreet dolore magna</p>
    <div class="btn">Read More</div>
    <div class="dots"><span></span><span class="on"></span><span></span><span></span><span></span></div>
  </section>

  <!-- services card -->
  <div class="abs card" style="left:159px">
    <svg class="frame" width="311" height="240" viewBox="0 0 311 240"><path d="M8 1H303Q310 1 310 8V238Q260 222 200 226Q140 232 70 236Q20 238 2 180V8Q2 1 8 1Z" fill="#fffdf8" stroke="#e4d7b8" stroke-width="1.5"/></svg>
    <div class="card-icon"><i></i></div>
    <h2>SERVICES</h2><div class="rule"></div>
    <div class="pic" role="img" aria-label="Woman in white lingerie sitting" style="left:195px;top:78px;width:110px;height:150px;background:radial-gradient(ellipse at 50% 50%,#f0d9c4 0%,rgba(255,253,248,0) 70%)"></div>
    <ul class="ticks">
      <li><svg width="13" height="10"><path d="M1 5l4 4 7-8" fill="none" stroke="#c8b07c" stroke-width="2"/></svg>Lorem ipsum dolor sit amet</li>
      <li><svg width="13" height="10"><path d="M1 5l4 4 7-8" fill="none" stroke="#c8b07c" stroke-width="2"/></svg>consectetuer cing elit</li>
      <li><svg width="13" height="10"><path d="M1 5l4 4 7-8" fill="none" stroke="#c8b07c" stroke-width="2"/></svg>sed diam nonummy nib</li>
      <li><svg width="13" height="10"><path d="M1 5l4 4 7-8" fill="none" stroke="#c8b07c" stroke-width="2"/></svg>euismod tincidunt ut laoreet</li>
      <li><svg width="13" height="10"><path d="M1 5l4 4 7-8" fill="none" stroke="#c8b07c" stroke-width="2"/></svg>dolore magna aliq</li>
      <li><svg width="13" height="10"><path d="M1 5l4 4 7-8" fill="none" stroke="#c8b07c" stroke-width="2"/></svg>am nonummy nib</li>
    </ul>
    <div class="more" style="left:130px">VIEW ALL</div>
  </div>

  <!-- care line card -->
  <div class="abs card" style="left:499px">
    <svg class="frame" width="311" height="240" viewBox="0 0 311 240"><path d="M8 1H303Q310 1 310 8V238Q260 222 200 226Q140 232 70 236Q20 238 2 180V8Q2 1 8 1Z" fill="#fffdf8" stroke="#e4d7b8" stroke-width="1.5"/></svg>
    <div class="card-icon"><i></i></div>
    <h2>CARE LINE</h2><div class="rule"></div>
    <div class="pic" role="img" aria-label="Hands massaging a leg" style="left:20px;top:85px;width:270px;height:63px;background:linear-gradient(90deg,#f6d8c4,#eec0a2 50%,#f8e4d6)"></div>
    <p class="copy">Lorem ipsum dolor sit amet, consectetuer adipiscing elit, sed diam nonummy nibh aliquam erat volutpat.</p>
    <div class="more" style="left:153px">READ MORE</div>
  </div>

  <!-- price lists card -->
  <div class="abs card" style="left:830px">
    <svg class="frame" width="311" height="240" viewBox="0 0 311 240"><path d="M8 1H303Q310 1 310 8V238Q260 222 200 226Q140 232 70 236Q20 238 2 180V8Q2 1 8 1Z" fill="#fffdf8" stroke="#e4d7b8" stroke-width="1.5"/></svg>
    <div class="card-icon"><i></i></div>
    <h2>PRICE LISTS</h2><div class="rule"></div>
    <div class="pic" role="img" aria-label="Candles and spa stones" style="left:20px;top:85px;width:270px;height:63px;background:linear-gradient(90deg,#3a1a08,#c0501a 18%,#2a1a10 32%,#8a5a30 45%,#e8e0c8 62%,#7fa83a 75%,#222 88%,#c6d87a)"></div>
    <div class="prices">
      <div>Lorem ipsum<em>..............................</em>$123</div>
      <div>consectetuer<em>..............................</em>$123</div>
      <div>sed diam non<em>..............................</em>$123</div>
    </div>
    <div class="more" style="left:186px">VIEW ALL</div>
  </div>

  <h2 class="abs welcome" style="font-weight:400">Welcome to <b>Kirelta</b></h2>
  <p class="abs welcome-text">Lorem ipsum dolor sit amet, consectetuer adipiscing elit, sed diam nonummy nibh euismod tincidunt ut laoreet dolore magna aliquam erat volutpat. Ut wisi enim ad minim veniam, quis nostrud exerciLorem ipsum dolor sit amet, consectetuer adipiscing elit, sed diam nonummy nibh euismod tincidunt ut laoreet dolore magna aliquam erat volutpat. Ut wisi enim ad minim veniam, quis nostrud exerciLorem ipsum dolor sit amet, consectetuer adipiscing elit, sed diam nonummy nibh euismod tincidunt ut laoreet dolore magna aliquam erat volutpat. Ut wisi enim ad minim veniam, quis nostrud exerciLorem ipsum dolor sit amet, consectetuer adipiscing elit, sed diam nonummy nibh euismod tincidunt ut laoreet dolore magna aliquam erat volutpat.</p>
  <div class="abs welcome-more">READ MORE</div>

  <aside class="abs offer">
    <div class="offer-photo" role="img" aria-label="Woman with a towel on her head, eyes closed"></div>
    <div class="offer-head">OFFER<span>OF THE</span>MONTH</div>
    <div class="offer-deal">20% OFF</div>
    <div class="offer-click">CLICK HERE</div>
  </aside>

  <footer class="abs footer"></footer>

  <div class="abs news">
    <h3>Join to Our Newsletter</h3>
    <div class="field">Enter your email</div>
    <div class="go">Sign Up</div>
    <div class="split"></div>
    <h4>Follow Us</h4>
    <div class="social"><span></span><span></span><span></span><span></span></div>
  </div>

  <h3 class="abs foot-h" style="left:161px;top:1165px">Gallery</h3>
  <svg class="abs" style="left:160px;top:1256px" width="14" height="24"><path d="M12 2L3 12l9 10" fill="none" stroke="#d6c395" stroke-width="3"/></svg>
  <div class="abs thumb" style="left:180px"><i role="img" aria-label="Woman with clear skin" style="background:linear-gradient(135deg,#f3d9c8,#a8d4ee)"></i></div>
  <div class="abs thumb" style="left:310px"><i role="img" aria-label="Eyelash treatment close-up" style="background:linear-gradient(135deg,#e8c7b5,#f2e4dc 60%,#d9bba8)"></i></div>
  <div class="abs thumb" style="left:440px"><i role="img" aria-label="Leg waxing treatment" style="background:linear-gradient(135deg,#f6efe6,#ebcdb4 60%,#f7f1ea)"></i></div>
  <svg class="abs" style="left:567px;top:1256px" width="14" height="24"><path d="M2 2l9 10-9 10" fill="none" stroke="#d6c395" stroke-width="3"/></svg>

  <h3 class="abs foot-h" style="left:653px;top:1165px">Contact Us</h3>
  <ul class="abs contact">
    <li><svg width="21" height="16"><path d="M2 6Q10 0 19 6L17 8 14 6V5Q10 3 7 5V6L4 8Z M5 9H16L18 15H3Z" fill="#fff"/></svg>012 345 6789</li>
    <li><svg width="21" height="18"><rect x="5" y="1" width="11" height="5" fill="#fff"/><rect x="1" y="6" width="19" height="8" rx="2" fill="#fff"/><rect x="5" y="11" width="11" height="6" fill="#fff" stroke="#333"/></svg>012 345 6789</li>
    <li><svg width="21" height="16"><rect x="2" y="2" width="17" height="12" fill="#fff"/><path d="M2 2l8.5 7L19 2" fill="none" stroke="#333" stroke-width="1.5"/></svg>info@kirelta.com</li>
    <li><svg width="21" height="24"><path d="M10.5 1a7 7 0 0 1 7 7c0 5-7 15-7 15S3.5 13 3.5 8a7 7 0 0 1 7-7Z" fill="#fff"/><circle cx="10.5" cy="8" r="2.6" fill="#333"/></svg>31, Lorem isad dsand<br>sdsafdsdf, aerrw</li>
  </ul>

  <div class="abs foot-brand"><span class="brand-dot"></span><span class="brand-name">kirelta</span></div>

  <div class="abs bottom">
    <nav><a>Home</a><a>About Us</a><a>Services</a><a>Gallery</a><a>Care Line</a><a>Offers</a><a>Price Lists</a><a>Contact Us</a></nav>
    <div class="copy">Copyright 2014 - Kirelta. All Rights Reserved</div>
  </div>
</div>
</body>
</html>
```